Business software developers new website

We need to redesign our website. Our current website is http://www.quorvanta.net/index.html, which is outdated and needs a new look. We moved out from web design and have concentrated more on the back end of the systems, for example, system support and security and cloud-based applications. Our major clients include both private and government sectors. We would like to see some designs that are all in one page, simple and clean. Prefer illustrator or obstructed images instead of real-life photos. Must look futuristic yet friendly. Attached the new logo for your references and good luck.

Target Market(s)

Medium to big company for their IT or data management. Either improve or upgrade their current system.

Industry/Entity Type

Business Software

Number of Pages Required

1 page

Colors

Designer to choose colors to be used in the design.

Requirements
Must have
• Simple and clean. Individual assets must be provided in the correct size and format(png or jpeg). Prefer Goggle fonts. Even though the logo color is red, grey and black, still prefer some modern colors that go well with red. When design, must consider the possibility to convert it into responsive.
Nice to have
• White background
Should not have
• real life photos, no slider

```html
<!DOCTYPE html>
<html lang="en">
<head>
<meta charset="utf-8">
<title>quorvanta.net — Software and Web Development Company</title>
<link rel="stylesheet" href="https://fonts.googleapis.com/css2?family=Roboto:wght@400;500;700&family=Nunito+Sans:wght@400;600;700&display=swap">
<style>
:root{
  --red:#e5323f;
  --orange:#ffb457;
  --pink:#ff3d5c;
  --navy:#1f1d3d;
  --ink:#2b2a33;
  --text:#3c3b46;
  --muted:#8a8a94;
  --field:#f4f5f7;
  --footer:#2b2a30;
  --white:#ffffff;
}
*{margin:0;padding:0;box-sizing:border-box}
html,body{width:1200px;height:3352px;overflow:hidden;background:var(--white)}
body{position:relative;font-family:"Nunito Sans",sans-serif;color:var(--text)}
.abs{position:absolute}

/* header */
.logo{left:76px;top:18px;font-family:"Roboto",sans-serif;font-size:42px;font-weight:400;color:var(--ink);letter-spacing:-0.5px;display:flex;align-items:center;gap:10px}
.logo-dot{width:12px;height:12px;background:var(--red);border-radius:50%}
.nav{top:46px;right:74px;display:flex;gap:48px;font-family:"Roboto",sans-serif;font-size:15px;font-weight:500;color:var(--ink)}

/* hero */
.hero-bg{left:0;top:75px}
.hero-art{left:590px;top:180px;width:560px;height:600px;border-radius:40px;background:radial-gradient(ellipse at 55% 45%,rgba(43,42,48,.14),rgba(229,50,63,.06) 55%,rgba(255,255,255,0) 75%)}
.hero-title{left:80px;top:290px;font-family:"Roboto",sans-serif;font-weight:700;font-size:27px;color:var(--white)}
.hero-sub{left:80px;top:382px;font-family:"Roboto",sans-serif;font-size:20px;line-height:24px;color:var(--white)}
.btn-outline{left:78px;top:501px;width:192px;height:60px;border:3px solid var(--white);color:var(--white);font-family:"Roboto",sans-serif;font-size:19px;display:flex;align-items:center;justify-content:center}

/* section titles */
.section-title{left:0;width:1200px;text-align:center;font-family:"Roboto",sans-serif;font-size:60px;color:var(--navy);font-weight:400;letter-spacing:-1px}
.section-title b{color:var(--red);font-weight:700}

.intro{left:76px;top:1023px;width:1050px;font-size:16px;line-height:27px;color:var(--text)}

/* service cards */
.service-card{top:1165px;width:300px;height:388px;background:var(--white);box-shadow:0 6px 22px rgba(30,30,60,.07);border-radius:4px;text-align:center}
.service-card svg{margin-top:38px}
.service-card h3{font-family:"Roboto",sans-serif;font-weight:500;font-size:21px;color:var(--navy);margin-top:10px}
.service-card p{text-align:left;font-size:14px;line-height:27px;color:var(--text);padding:22px 18px 0 18px}

/* tech cards */
.tech-card{width:463px;height:183px;background:var(--white);box-shadow:0 6px 22px rgba(30,30,60,.08);border-radius:3px}
.tech-icon{position:absolute;left:32px;top:50px}
.tech-card h4{position:absolute;left:132px;top:54px;font-family:"Roboto",sans-serif;font-weight:500;font-size:14px;color:var(--ink)}
.tech-card p{position:absolute;left:132px;top:86px;width:300px;font-family:"Roboto",sans-serif;font-size:11.5px;line-height:19px;color:var(--ink);text-align:justify}

/* testimonial */
.testimonials{left:0;top:2298px;width:1200px;height:415px;background:var(--red);overflow:hidden}
.t-title{top:48px;left:0;width:1200px;text-align:center;font-family:"Roboto",sans-serif;font-weight:700;font-size:60px;color:var(--white);letter-spacing:-1px}
.t-quote{top:170px;left:195px;width:810px;font-family:"Roboto",sans-serif;font-weight:500;font-size:13.5px;line-height:30px;color:var(--white)}
.t-name{top:295px;left:0;width:1200px;text-align:center;font-family:"Roboto",sans-serif;font-weight:700;font-size:11px;letter-spacing:1px;color:var(--white)}

/* contact */
.hello-title{top:2810px;font-weight:700;font-size:50px}
.hello-title .small{font-size:42px}
.field{background:var(--field);font-size:15px;color:var(--muted);padding:12px 16px}
.btn-submit{left:76px;top:3140px;width:668px;height:42px;background:var(--red);color:var(--white);font-family:"Roboto",sans-serif;font-weight:700;font-size:13px;display:flex;align-items:center;justify-content:center;border-radius:2px}
.contact-info{left:820px;top:2921px;width:290px;font-size:14px;line-height:30px;color:var(--ink)}
.socials{left:820px;top:3126px;display:flex;gap:14px}
.socials span{width:32px;height:32px;border-radius:50%;border:1px solid #e9e9ee;box-shadow:0 2px 6px rgba(0,0,0,.06);display:flex;align-items:center;justify-content:center}
.socials span i{width:8px;height:8px;border-radius:50%;background:var(--red)}

.footer{left:0;top:3276px;width:1200px;height:76px;background:var(--footer);color:var(--white);font-family:"Roboto",sans-serif;font-size:15px;display:flex;align-items:center;justify-content:center}
</style>
</head>
<body>

<header>
  <div class="abs logo"><span>quorvanta.net</span><span class="logo-dot"></span></div>
  <nav class="abs nav"><span>Home</span><span>Service</span><span>Clients</span><span>Contact</span></nav>
</header>

<section class="hero">
  <svg class="abs hero-bg" width="1200" height="748" viewBox="0 0 1200 748">
    <defs>
      <linearGradient id="heroFill" x1="0" y1="0" x2="1" y2="1">
        <stop offset="0" stop-color="#ffb25a"/>
        <stop offset="0.35" stop-color="#f0603f"/>
        <stop offset="0.7" stop-color="#e5323f"/>
        <stop offset="1" stop-color="#e5323f"/>
      </linearGradient>
      <linearGradient id="circleA" x1="0" y1="0" x2="1" y2="1">
        <stop offset="0" stop-color="#ffb457"/>
        <stop offset="1" stop-color="#ff3d5c"/>
      </linearGradient>
      <linearGradient id="circleB" x1="1" y1="0" x2="0" y2="1">
        <stop offset="0" stop-color="#ff3d5c"/>
        <stop offset="1" stop-color="#ffa25a"/>
      </linearGradient>
    </defs>
    <path d="M0 0 H696 C692 150 660 250 580 320 C480 400 396 440 397 520 C398 620 500 705 640 748 H0 Z" fill="url(#heroFill)"/>
    <circle cx="308" cy="35" r="145" fill="url(#circleA)" opacity=".9"/>
    <circle cx="-10" cy="670" r="180" fill="url(#circleB)" opacity=".85"/>
  </svg>
  <div class="abs hero-art" role="img" aria-label="Illustration of developers working at a large monitor with code, a keyboard, a light bulb and a security shield"></div>
  <h1 class="abs hero-title">Software and Web Development Company</h1>
  <p class="abs hero-sub">Provides individual technology solutions<br>and professional software for clients worldwide</p>
  <div class="abs btn-outline">READ MORE</div>
</section>

<section class="services">
  <h2 class="abs section-title" style="top:900px">Our <b>Services</b></h2>
  <p class="abs intro">We have provided web design, graphic design and application development solutions for a wide variety of industries. We are known for the quality of our work, affordable rates and our individual approach to each customer. Our company offers a wide variety of professional web solution and all this at very competitive prices!</p>

  <article class="abs service-card" style="left:78px">
    <svg width="44" height="40" viewBox="0 0 44 40"><path d="M22 4 L8 34 M22 4 L36 34 M12 24 H32" stroke="#e5323f" stroke-width="4" fill="none" stroke-linecap="round"/><circle cx="22" cy="6" r="4" fill="#e5323f"/></svg>
    <h3>Web Design</h3>
    <p>Your website needs the 'wow' factor to meet you're audiences needs. Without this, you won't entice visitors to look beyond the homepage. Our web designers understand that beauty is more than skin deep ensuring your site is appealing, quick loading, relevant and goal driven..</p>
  </article>
  <article class="abs service-card" style="left:446px">
    <svg width="44" height="40" viewBox="0 0 44 40"><rect x="6" y="4" width="32" height="24" rx="2" fill="#e5323f"/><rect x="18" y="28" width="8" height="6" fill="#e5323f"/><rect x="12" y="34" width="20" height="3" fill="#e5323f"/><path d="M15 16 l5 5 l9 -9" stroke="#fff" stroke-width="3" fill="none"/></svg>
    <h3>Software Development</h3>
    <p>We build robust, reliable websites – and make sure they stay that way. We cover all your online needs, from building a Website that you can edit yourself, to adding tools like Shopping Carts, Event Managers, Blogs and communication etc, before implementing an effective Search Engine Optimisation program to drive traffic there.</p>
  </article>
  <article class="abs service-card" style="left:826px">
    <svg width="44" height="40" viewBox="0 0 44 40"><path d="M8 24 L28 8 L34 28 Z" fill="#e5323f"/><rect x="8" y="22" width="8" height="10" fill="#e5323f" transform="rotate(-30 12 27)"/><path d="M34 6 l4 -3 M37 14 h5" stroke="#e5323f" stroke-width="2"/></svg>
    <h3>Marketing</h3>
    <p>Beside using the latest techniques to improve your Search Engine Ranking and make your site visible to your clients and the world, we can also setup your own monthly newsletters or promotional emails, which you have full control with your own mailing lists.</p>
  </article>
</section>

<section class="technologies">
  <h2 class="abs section-title" style="top:1636px">Our <b>Technologies</b></h2>

  <svg width="0" height="0" style="position:absolute">
    <defs>
      <linearGradient id="techGrad" x1="0" y1="0" x2="1" y2="1">
        <stop offset="0" stop-color="#ffa25a"/><stop offset="1" stop-color="#e5323f"/>
      </linearGradient>
    </defs>
  </svg>

  <article class="abs tech-card" style="left:80px;top:1762px">
    <svg class="tech-icon" width="80" height="80" viewBox="0 0 80 80"><circle cx="40" cy="40" r="38" fill="none" stroke="#fbd3d6" stroke-width="2"/><circle cx="40" cy="40" r="32" fill="none" stroke="#f5a3aa" stroke-width="2"/><circle cx="40" cy="40" r="26" fill="url(#techGrad)"/><circle cx="40" cy="40" r="19" fill="none" stroke="#fff" stroke-width="1.5"/><path d="M34 34 l-6 6 l6 6 M46 34 l6 6 l-6 6 M43 32 l-6 16" stroke="#fff" stroke-width="2" fill="none"/></svg>
    <h4>Programming</h4>
    <p>We specialize in a variety of programming languages. We aim to deliver the best user experience to our customers without sacrificing security, performance and stability.</p>
  </article>
  <article class="abs tech-card" style="left:661px;top:1762px">
    <svg class="tech-icon" width="80" height="80" viewBox="0 0 80 80"><circle cx="40" cy="40" r="38" fill="none" stroke="#fbd3d6" stroke-width="2"/><circle cx="40" cy="40" r="32" fill="none" stroke="#f5a3aa" stroke-width="2"/><circle cx="40" cy="40" r="26" fill="url(#techGrad)"/><circle cx="40" cy="40" r="19" fill="none" stroke="#fff" stroke-width="1.5"/><rect x="33" y="29" width="14" height="22" rx="2" fill="none" stroke="#fff" stroke-width="2"/><circle cx="40" cy="46" r="1.6" fill="#fff"/></svg>
    <h4>Mobile Applications</h4>
    <p>Our mobile app developers focus on enhancing the 'ROI value' of these applications. With skilled and talented creative mobile app programmers we assure the real time value for every app</p>
  </article>
  <article class="abs tech-card" style="left:80px;top:2012px">
    <svg class="tech-icon" width="80" height="80" viewBox="0 0 80 80"><circle cx="40" cy="40" r="38" fill="none" stroke="#fbd3d6" stroke-width="2"/><circle cx="40" cy="40" r="32" fill="none" stroke="#f5a3aa" stroke-width="2"/><circle cx="40" cy="40" r="26" fill="url(#techGrad)"/><circle cx="40" cy="40" r="19" fill="none" stroke="#fff" stroke-width="1.5"/><path d="M31 40 l6 6 l12 -12" stroke="#fff" stroke-width="2.5" fill="none"/></svg>
    <h4>W3C Complaints</h4>
    <p>All of our sites are W3C compliant, so you never have to worry about incompatiblities between browsers.</p>
  </article>
  <article class="abs tech-card" style="left:663px;top:2012px">
    <svg class="tech-icon" width="80" height="80" viewBox="0 0 80 80"><circle cx="40" cy="40" r="38" fill="none" stroke="#fbd3d6" stroke-width="2"/><circle cx="40" cy="40" r="32" fill="none" stroke="#f5a3aa" stroke-width="2"/><circle cx="40" cy="40" r="26" fill="url(#techGrad)"/><circle cx="40" cy="40" r="19" fill="none" stroke="#fff" stroke-width="1.5"/><rect x="32" y="31" width="16" height="6" rx="1" fill="none" stroke="#fff" stroke-width="2"/><rect x="32" y="39" width="16" height="6" rx="1" fill="none" stroke="#fff" stroke-width="2"/><path d="M40 45 v5 M35 50 h10" stroke="#fff" stroke-width="2"/></svg>
    <h4>Hosting Solutions</h4>
    <p>We offer competitive hosting solutions with all of our projects so you never have to worry about finding your site the right home.</p>
  </article>
</section>

<section class="abs testimonials">
  <svg class="abs" style="left:0;top:0" width="1200" height="415" viewBox="0 0 1200 415">
    <defs>
      <linearGradient id="tGrad" x1="0" y1="0" x2="1" y2="1">
        <stop offset="0" stop-color="#ffa25a"/><stop offset="1" stop-color="#ff3d5c"/>
      </linearGradient>
    </defs>
    <circle cx="-10" cy="45" r="86" fill="url(#tGrad)"/>
    <circle cx="86" cy="395" r="78" fill="url(#tGrad)"/>
    <circle cx="1210" cy="368" r="118" fill="url(#tGrad)"/>
  </svg>
  <h2 class="abs t-title">What Our Customers Say</h2>
  <p class="abs t-quote">«Quorvanta.net got us top rankings on all of the major search engines where in the past we were unable to even show up on them. Quorvanta.net did what they promised, when they promised, all at a fair price.I'm very happy with my site!"</p>
  <p class="abs t-name">- DARA WENLOW</p>
</section>

<section class="contact">
  <h2 class="abs section-title hello-title">Say <b>Hello</b> <span class="small">to us</span></h2>
  <div class="abs field" style="left:76px;top:2930px;width:251px;height:42px">Your Name</div>
  <div class="abs field" style="left:76px;top:2992px;width:251px;height:42px">Email</div>
  <div class="abs field" style="left:76px;top:3055px;width:251px;height:42px">Subject</div>
  <div class="abs field" style="left:356px;top:2930px;width:388px;height:167px">Type your message</div>
  <div class="abs btn-submit">SUBMIT</div>

  <div class="abs contact-info">
    <p>As web developers, we understand that a powerful and functional web site is a vital component of modern day marketing for companies of today.</p>
    <p>Office number: +61 7 5550 0142</p>
    <p>Mobile number: +61 0400 555 318</p>
  </div>
  <div class="abs socials" aria-label="Social profiles">
    <span><i></i></span><span><i></i></span><span><i></i></span><span><i></i></span>
  </div>
</section>

<footer class="abs footer">© Copyright quorvanta. All Rights Reserved</footer>

</body>
</html>
```